Report Design Template Needed for Strategy Consulting Co.

I have a small consulting business that does market research, develops marketing strategy, and does business development work (sales, finding partners, preparing for investors) for small and medium-sized companies who can’t afford their own full-time marketing person.

Most of my reports are PowerPoint Decks. There is usually a Title Page, a Table of Contents, an Executive Summary, a Detailed Findings section (with some section breaks, so I need a divider page between sections), and a Recommendations section.

I need a report template/style that is attractive, professional and not too bold such that it takes away from the content, which is what they are paying for.

I have color palette ideas and graphics in the attached brief. Please let me know if you need anything else, or if you need graphic files.

Thank you!!

Target Market(s)

Small business professionals, scientists, business development executives.

Industry/Entity Type

Marketing

Font styles to use
Sans Serif

Requirements
Must have
• Should have the sections listed in the brief. Also, need to be able to import the template complete.
Should not have
• Background must not overtake the text

```html
<!DOCTYPE html>
<html lang="en">
<head>
<meta charset="utf-8">
<title>Meridian Partners – Report Template</title>
<link href="https://fonts.googleapis.com/css2?family=Aldrich&family=Open+Sans:wght@400;600&display=swap" rel="stylesheet">
<style>
:root{
  --navy:#1d4f6b;
  --green:#8fa83a;
  --green-light:#d3df9c;
  --green-mid:#b0c05a;
  --grey-dark:#5b5b5b;
  --grey-mid:#8a8a8a;
  --grey-light:#c3c3c3;
  --ink:#3b3b3b;
  --sky:#e6eef8;
  --board:#000;
}
*{box-sizing:border-box;margin:0;padding:0}
html,body{width:1052px;height:1200px;overflow:hidden;background:var(--board)}
body{position:relative;font-family:"Open Sans",sans-serif;color:var(--ink)}
.slide{position:absolute;width:495px;height:371px;overflow:hidden;
  background:radial-gradient(ellipse at 30% 45%,#dde8f5 0%,#f2f6fb 45%,#fbfcfe 80%)}
.col-l{left:14px}.col-r{left:534px}
.row-1{top:12px}.row-2{top:407px}.row-3{top:802px}
.header{position:absolute;left:0;top:0;width:100%;height:37px;background:var(--navy);border-bottom:3px solid var(--green)}
.header h1,.band h1{font-family:"Aldrich",sans-serif;font-weight:400;color:#fff;font-size:20px;letter-spacing:1px;line-height:37px;padding-left:9px}
.footer{position:absolute;left:0;bottom:0;width:100%;height:40px;border-top:1px solid var(--green);background:rgba(255,255,255,.85)}
.copyright{position:absolute;left:10px;bottom:14px;font-size:7px;letter-spacing:.4px;color:var(--navy)}
.brand{position:absolute;right:9px;font-weight:600;color:var(--navy);letter-spacing:-.5px;white-space:nowrap}
.footer .brand{bottom:9px;font-size:17px}
.photo{position:absolute;background:linear-gradient(135deg,#eef3fa,#b7c8de 55%,#7f95b3)}
/* cover */
.cover{background:#fff}
.cover .photo{left:0;top:0;width:100%;height:232px;background:linear-gradient(100deg,#dfe8f4 0%,#b9c9e0 40%,#4c5f80 70%,#c8d3e4 100%)}
.band{position:absolute;left:0;top:232px;width:100%;height:52px;background:var(--navy);border-bottom:4px solid var(--green);text-align:right}
.band h1{line-height:52px;padding-right:9px}
.cover .brand{bottom:28px;font-size:29px;right:11px}
/* text columns */
h2{font-family:"Open Sans",sans-serif;font-weight:400;font-size:14px;color:var(--navy);position:absolute}
.copy{position:absolute;font-size:7.6px;line-height:13.6px;color:var(--ink)}
.copy p+p{margin-top:13.6px}
.thumb{width:213px;height:74px;border:2px solid #fff;box-shadow:0 0 0 1px #d8e0ea;background:linear-gradient(100deg,#9ab3cf 0%,#8a5d3e 45%,#b3865e 70%,#a9c1da 100%)}
/* agenda */
.agenda-title{position:absolute;left:14px;top:56px;font-family:"Aldrich",sans-serif;font-size:16px;color:var(--navy);letter-spacing:1px}
.agenda-item{position:absolute;width:225px;height:28px;background:#fff;border:1px solid #dfe5ec;display:flex;align-items:center}
.agenda-item .num{width:25px;height:100%;background:var(--navy);color:#fff;font-family:"Aldrich",sans-serif;font-size:15px;display:flex;align-items:center;justify-content:center;border-right:3px solid var(--green)}
.agenda-item .label{padding-left:10px;font-family:"Aldrich",sans-serif;font-size:13px;color:var(--navy)}
/* contact */
.contact .brand{left:32px;right:auto;top:147px;font-size:22px}
.divider{position:absolute;left:246px;top:72px;width:1px;height:176px;background:#d6dde6}
.contact-lines{position:absolute;left:269px;top:98px;font-size:9.3px;line-height:14px;color:#222}
.contact-row{position:absolute;left:269px;display:flex;align-items:center;font-size:9.3px;color:#222}
.contact-row svg{margin-right:8px}
.contact .copyright{bottom:8px}
.contact .footer{height:32px;border-top:none}
</style>
</head>
<body>

<!-- cover -->
<section class="slide cover col-l row-1">
  <div class="photo" role="img" aria-label="Photo of a business team meeting in a bright office"></div>
  <div class="band"><h1>PROJECT TITLE HERE</h1></div>
  <div class="brand">Meridian Partners</div>
</section>

<!-- two column content -->
<section class="slide col-r row-1">
  <header class="header"><h1>PROJECT TITLE HERE</h1></header>
  <h2 style="left:14px;top:78px">Lorem ipsum dolor sit ipsum</h2>
  <div class="photo thumb" style="left:14px;top:98px" role="img" aria-label="Photo of a smiling homeowner in front of a brick house"></div>
  <div class="copy" style="left:15px;top:180px;width:225px">
    <p>Lorem ipsum dolor sit ipsum Lorem ipsum dolor sit ipsum Lorem ipsum dolor sit ipsum Lorem ipsum dolor sit ipsum lorem ipsum dolor sit ipsum Lorem ipsum dolor sit ipsum Lorem ipsum dolor sit ipsum</p>
    <p>Lorem ipsum dolor sit ipsum Lorem ipsum dolor sit ipsum Lorem ipsum dolor sit ipsum Lorem ipsum dolor sit ipsum lorem ipsum dolor sit ipsum Lorem ipsum dolor sit ipsum Lorem ipsum dolor sit ipsum</p>
  </div>
  <h2 style="left:262px;top:78px">Lorem ipsum dolor sit ipsum</h2>
  <div class="photo thumb" style="left:262px;top:98px" role="img" aria-label="Photo of a smiling homeowner in front of a brick house"></div>
  <div class="copy" style="left:263px;top:180px;width:225px">
    <p>Lorem ipsum dolor sit ipsum Lorem ipsum dolor sit ipsum Lorem ipsum dolor sit ipsum Lorem ipsum dolor sit ipsum lorem ipsum dolor sit ipsum Lorem ipsum dolor sit ipsum Lorem ipsum dolor sit ipsum</p>
    <p>Lorem ipsum dolor sit ipsum Lorem ipsum dolor sit ipsum Lorem ipsum dolor sit ipsum Lorem ipsum dolor sit ipsum lorem ipsum dolor sit ipsum Lorem ipsum dolor sit ipsum Lorem ipsum dolor sit ipsum</p>
  </div>
  <footer class="footer"><span class="copyright">COPYRIGHT TEXT HERE</span><span class="brand">Meridian Partners</span></footer>
</section>

<!-- chart -->
<section class="slide col-l row-2">
  <header class="header"><h1>PROJECT TITLE HERE</h1></header>
  <h2 style="left:15px;top:73px">Lorem ipsum dolor sit ipsum</h2>
  <div class="copy" style="left:15px;top:99px;width:225px">
    <p>Lorem ipsum dolor sit ipsum Lorem ipsum dolor sit ipsum Lorem ipsum dolor sit ipsum Lorem ipsum dolor sit ipsum lorem ipsum dolor sit ipsum Lorem ipsum dolor sit ipsum Lorem ipsum dolor sit ipsum</p>
    <p>Lorem ipsum dolor sit ipsum Lorem ipsum dolor sit ipsum Lorem ipsum dolor sit ipsum Lorem ipsum dolor sit ipsum lorem ipsum dolor sit ipsum Lorem ipsum dolor sit ipsum Lorem ipsum dolor sit ipsum</p>
    <p>Lorem ipsum dolor sit ipsum Lorem ipsum dolor sit ipsum Lorem ipsum dolor sit ipsum Lorem ipsum dolor sit ipsum Lorem ipsum dolor sit ipsum</p>
  </div>
  <svg class="pie-chart" style="position:absolute;left:270px;top:86px" width="206" height="206" viewBox="-103 -103 206 206" font-family="Open Sans, sans-serif" font-size="7" text-anchor="middle">
    <g stroke="#fff" stroke-width="1.5">
      <path d="M0 0 L0 -96 A96 96 0 0 1 48 -83.1Z" fill="var(--grey-light)"/>
      <path d="M0 0 L48 -83.1 A96 96 0 0 1 94.5 16.7Z" fill="var(--green-light)"/>
      <path d="M0 0 L94.5 16.7 A96 96 0 0 1 40.6 87Z" fill="var(--green-mid)"/>
      <path d="M0 0 L40.6 87 A96 96 0 0 1 -87 40.6Z" fill="var(--navy)"/>
      <path d="M0 0 L-87 40.6 A96 96 0 0 1 -61.7 -73.5Z" fill="var(--grey-dark)"/>
      <path d="M0 0 L-61.7 -73.5 A96 96 0 0 1 0 -96Z" fill="var(--grey-mid)"/>
    </g>
    <circle r="16" fill="#fff" stroke="var(--green)" stroke-width="2"/>
    <g fill="#222"><text x="19" y="-70">Lorem</text><text x="19" y="-61">ipsum</text><text x="19" y="-52">dolor</text></g>
    <g fill="#fff"><text x="-18" y="-70">Lorem</text><text x="-18" y="-61">ipsum</text><text x="-18" y="-52">dolor</text></g>
    <g fill="#222"><text x="58" y="-12">Lorem ipsum</text><text x="56" y="-3">dolor</text></g>
    <g fill="#222"><text x="46" y="42">Lorem ipsum</text><text x="44" y="51">dolor</text></g>
    <g fill="#fff"><text x="-27" y="59">Lorem ipsum dolor</text><text x="-27" y="68">Lorem ipsum dolor</text></g>
    <g fill="#fff"><text x="-53" y="-2">Lorem ipsum dolor</text><text x="-53" y="7">Lorem ipsum dolor</text></g>
  </svg>
  <footer class="footer"><span class="copyright">COPYRIGHT TEXT HERE</span><span class="brand">Meridian Partners</span></footer>
</section>

<!-- agenda -->
<section class="slide col-r row-2">
  <header class="header"><h1>PROJECT TITLE HERE</h1></header>
  <div class="agenda-title">AGENDA SLIDE</div>
  <div class="agenda-item" style="left:14px;top:78px"><span class="num">01</span><span class="label">Slide Title Here</span></div>
  <div class="agenda-item" style="left:14px;top:126px"><span class="num">01</span><span class="label">Slide Title Here</span></div>
  <div class="agenda-item" style="left:14px;top:173px"><span class="num">01</span><span class="label">Slide Title Here</span></div>
  <div class="agenda-item" style="left:14px;top:221px"><span class="num">01</span><span class="label">Slide Title Here</span></div>
  <div class="agenda-item" style="left:14px;top:268px"><span class="num">01</span><span class="label">Slide Title Here</span></div>
  <div class="agenda-item" style="left:258px;top:78px"><span class="num">01</span><span class="label">Slide Title Here</span></div>
  <div class="agenda-item" style="left:258px;top:126px"><span class="num">01</span><span class="label">Slide Title Here</span></div>
  <div class="agenda-item" style="left:258px;top:173px"><span class="num">01</span><span class="label">Slide Title Here</span></div>
  <div class="agenda-item" style="left:258px;top:221px"><span class="num">01</span><span class="label">Slide Title Here</span></div>
  <div class="agenda-item" style="left:258px;top:268px"><span class="num">01</span><span class="label">Slide Title Here</span></div>
  <footer class="footer"><span class="copyright">COPYRIGHT TEXT HERE</span><span class="brand">Meridian Partners</span></footer>
</section>

<!-- blank / divider -->
<section class="slide col-l row-3">
  <header class="header"><h1>PROJECT TITLE HERE</h1></header>
  <footer class="footer"><span class="copyright">COPYRIGHT TEXT HERE</span><span class="brand">Meridian Partners</span></footer>
</section>

<!-- contact -->
<section class="slide contact col-r row-3">
  <header class="header"><h1>PROJECT TITLE HERE</h1></header>
  <div class="brand">Meridian Partners</div>
  <div class="divider"></div>
  <div class="contact-lines">Contact Details line here Contact Details<br>line here, Contact Details line here</div>
  <div class="contact-row" style="top:148px">
    <svg width="14" height="14" viewBox="0 0 14 14"><circle cx="7" cy="7" r="7" fill="var(--green)"/><path d="M4.4 3.6l1.5-.3.8 1.8-.9.7a5 5 0 0 0 2.3 2.3l.7-.9 1.8.8-.3 1.5c-3.3.2-6.2-2.7-5.9-5.9z" fill="#fff"/></svg>
    01 2345 678900</div>
  <div class="contact-row" style="top:175px">
    <svg width="14" height="14" viewBox="0 0 14 14"><circle cx="7" cy="7" r="7" fill="var(--green)"/><rect x="3.5" y="4.5" width="7" height="5" fill="none" stroke="#fff" stroke-width="1"/><path d="M3.5 4.5l3.5 2.8 3.5-2.8" fill="none" stroke="#fff" stroke-width="1"/></svg>
    hello@meridianpartners.com</div>
  <div class="contact-row" style="top:202px">
    <svg width="14" height="14" viewBox="0 0 14 14"><circle cx="7" cy="7" r="7" fill="var(--green)"/><circle cx="7" cy="7" r="3.6" fill="none" stroke="#fff" stroke-width="1"/><path d="M3.4 7h7.2M7 3.4c-1.6 2-1.6 5.2 0 7.2M7 3.4c1.6 2 1.6 5.2 0 7.2" fill="none" stroke="#fff" stroke-width=".8"/></svg>
    www.meridianpartners.com</div>
  <footer class="footer"><span class="copyright">COPYRIGHT TEXT HERE</span></footer>
</section>

</body>
</html>
```